Business Card Design

Marla Quibbet
Artist of Contemporary/Modern/Representational Art
Contact: 0457219308
Please include my web site (thanks)! http://www.artvault913.com.au/marla-quibbet
And
Email: marlaquibbet@fernpost.example

Target Market(s)

Modern professional People who know what they like in modern contemporary art and have the means to purchase it.

Industry/Entity Type

Business

Contact Information for Business Card

Marla Quibbet
Contact: 0457219308

Font styles to use
Sans Serif

Requirements
Must have
• Simplicity & to the point
Keep the font modern/ contemporary
Nice to have
• A portrait of me and one piece of work on the business card (one on each side).
Should not have
• I'm not into butterflies.
No feminine style swirls
Nor I like swirls that look like tatoos

```html
<!DOCTYPE html>
<html lang="en">
<head>
<meta charset="utf-8">
<title>Marla Quibbet — Business Card</title>
<link rel="stylesheet" href="https://fonts.googleapis.com/css2?family=Oswald:wght@500;600&family=PT+Sans:ital@1&display=swap">
<style>
  :root {
    --backdrop: #eeece8;
    --card: #0a0a0a;
    --ink: #ffffff;
    --ink-soft: #e6e6e6;
    --portrait-hair: #4a4540;
    --portrait-skin: #c9a08c;
    --portrait-scarf: #e0622a;
  }
  * { margin: 0; padding: 0; box-sizing: border-box; }
  html, body {
    width: 849px; height: 1200px; overflow: hidden;
    background: var(--backdrop);
  }
  .canvas { position: relative; width: 849px; height: 1200px; }

  .card {
    position: absolute;
    background: var(--card);
    color: var(--ink);
    overflow: hidden;
  }
  .card--front { left: 51px; top: 118px; width: 754px; height: 464px; }
  .card--back  { left: 57px; top: 627px; width: 753px; height: 465px; }

  .portrait {
    position: absolute; left: 0; top: 0; width: 330px; height: 464px;
    background:
      radial-gradient(ellipse 38% 30% at 45% 48%, var(--portrait-skin) 0%, rgba(201,160,140,0) 100%),
      radial-gradient(ellipse 55% 30% at 40% 95%, var(--portrait-scarf) 0%, rgba(224,98,42,0) 100%),
      linear-gradient(180deg, var(--portrait-hair) 0%, #2e2a27 60%, #1a1512 100%);
    -webkit-mask-image: linear-gradient(90deg, #000 62%, transparent 100%);
            mask-image: linear-gradient(90deg, #000 62%, transparent 100%);
  }

  .identity {
    position: absolute; right: 42px; top: 22px; text-align: right;
  }
  .identity__name {
    font-family: "Oswald", sans-serif; font-weight: 600;
    font-size: 70px; line-height: 1.1; letter-spacing: 0.5px;
  }
  .identity__title {
    margin-top: 4px;
    font-family: "PT Sans", sans-serif; font-style: italic;
    font-size: 13.5px; color: var(--ink-soft);
  }

  .contact {
    position: absolute; right: 42px; top: 290px; text-align: right;
    font-family: "Oswald", sans-serif; font-weight: 500;
  }
  .contact__phone { font-size: 37px; line-height: 1.1; }
  .contact__email { margin-top: 18px; font-size: 21px; }
  .contact__web   { margin-top: 12px; font-size: 21px; }

  .artwork { position: absolute; }
  .artwork--street   { left: 46px;  top: 62px;  width: 210px; height: 160px;
    background: linear-gradient(135deg, #d9b54a 0%, #d85a7a 45%, #8b8f92 75%, #e6e6e6 100%); }
  .artwork--facades  { left: 497px; top: 57px;  width: 212px; height: 162px;
    background: linear-gradient(90deg, #d63b2e 0%, #e6c23a 30%, #5f9a4a 55%, #4b7bc0 75%, #d9453a 100%); }
  .artwork--harbour  { left: 138px; top: 253px; width: 213px; height: 163px;
    background: linear-gradient(160deg, #3c4a52 0%, #c4563a 40%, #e09a4a 65%, #35505a 100%); }
  .artwork--city     { left: 417px; top: 254px; width: 212px; height: 162px;
    background: linear-gradient(160deg, #6f8c9a 0%, #4f8e5a 40%, #3a6f9c 65%, #d9d3c7 100%); }

  .tagline {
    position: absolute; left: 229px; top: 76px; width: 300px; text-align: center;
    font-family: "Oswald", sans-serif; font-weight: 500;
    font-size: 22px; line-height: 31px;
  }
</style>
</head>
<body>
<main class="canvas">
  <section class="card card--front">
    <div class="portrait" role="img" aria-label="Portrait photograph of the artist"></div>
    <div class="identity">
      <h1 class="identity__name">Marla Quibbet</h1>
      <p class="identity__title">Artist of Contemporary/Modern/Representational Art</p>
    </div>
    <div class="contact">
      <p class="contact__phone">0457219308</p>
      <p class="contact__email">marla@marlaquibbet.com.au</p>
      <p class="contact__web">www.artvault913.com.au/marla-quibbet</p>
    </div>
  </section>

  <section class="card card--back">
    <div class="artwork artwork--street" role="img" aria-label="Painting of a street with bare trees and a pink house"></div>
    <div class="artwork artwork--facades" role="img" aria-label="Painting of a row of colourful townhouse facades"></div>
    <p class="tagline">Artist of<br>Contemporary<br>Modern<br>Representational Art</p>
    <div class="artwork artwork--harbour" role="img" aria-label="Painting of a red-roofed old town by the water"></div>
    <div class="artwork artwork--city" role="img" aria-label="Painting of a city skyline with river and stadiums"></div>
  </section>
</main>
</body>
</html>
```